Email Signatures

I would like to create a new email signature for my team. The design will be the same for everyone, with only individual details such as name and email changing. You can also see our brand style on our website. https://www.tlmbespokehomes.com.au/

Target Market(s)

Clients for new builds or renovations

Industry/Entity Type

Construction

Colors

Designer to choose colors to be used in the design.

```html
<!DOCTYPE html>
<html lang="en">
<head>
<meta charset="UTF-8">
<title>TLM Email Signature – Liam Hartley</title>
<link rel="stylesheet" href="https://fonts.googleapis.com/css2?family=Rubik:wght@400;500;700;800&display=swap">
<style>
  :root {
    --bg: #ebe8e1;
    --green: #1a9f48;
    --ink: #1f2321;
    --white: #ffffff;
    --photo-light: #b9b6b1;
    --photo-dark: #4a4c4d;
  }
  * { margin: 0; padding: 0; box-sizing: border-box; }
  html, body {
    width: 1200px;
    height: 384px;
    overflow: hidden;
    background: var(--bg);
  }
  .signature {
    position: relative;
    width: 1200px;
    height: 384px;
    overflow: hidden;
    background: var(--bg);
    font-family: "Rubik", sans-serif;
    color: var(--ink);
  }
  .decor { position: absolute; inset: 0; }
  .brand-name {
    position: absolute;
    left: 36px;
    top: 38px;
    font-size: 46px;
    font-weight: 800;
    letter-spacing: 1px;
    color: var(--ink);
    line-height: 1;
  }
  .person {
    position: absolute;
    left: 36px;
    top: 156px;
  }
  .person-name {
    font-size: 44px;
    font-weight: 400;
    color: var(--green);
    line-height: 1.1;
  }
  .person-role {
    margin-top: 10px;
    font-size: 23px;
    font-weight: 400;
    color: var(--ink);
  }
  .portrait {
    position: absolute;
    left: 386px;
    top: 66px;
    width: 268px;
    height: 268px;
    border-radius: 50%;
    border: 3px solid var(--green);
    background: var(--white);
    padding: 11px;
  }
  .portrait-fill {
    width: 100%;
    height: 100%;
    border-radius: 50%;
    background: radial-gradient(circle at 50% 40%, var(--photo-light) 0%, #8f8c88 55%, var(--photo-dark) 100%);
  }
  .contacts {
    position: absolute;
    left: 738px;
    top: 86px;
    list-style: none;
  }
  .contact {
    display: flex;
    align-items: center;
    height: 52px;
    font-size: 22px;
    color: var(--ink);
  }
  .contact svg { width: 26px; height: 26px; margin-right: 12px; flex: none; }
  .socials {
    position: absolute;
    left: 744px;
    top: 246px;
    display: flex;
    gap: 12px;
  }
  .social {
    width: 38px;
    height: 38px;
    border-radius: 50%;
    border: 2.5px solid var(--green);
  }
</style>
</head>
<body>
<main class="signature">
  <svg class="decor" width="1200" height="384" viewBox="0 0 1200 384" aria-hidden="true">
    <circle cx="820" cy="-190" r="240" fill="var(--green)"/>
    <circle cx="1205" cy="-5" r="72" fill="var(--green)"/>
    <circle cx="0" cy="388" r="70" fill="var(--green)"/>
    <circle cx="432" cy="462" r="150" fill="var(--green)"/>
  </svg>

  <div class="brand-name">TLM</div>

  <section class="person">
    <h1 class="person-name">Liam Hartley</h1>
    <p class="person-role">General Manager</p>
  </section>

  <div class="portrait">
    <div class="portrait-fill" role="img" aria-label="Portrait photo of Liam Hartley"></div>
  </div>

  <ul class="contacts">
    <li class="contact">
      <svg viewBox="0 0 24 24" fill="none" stroke="var(--green)" stroke-width="1.8" stroke-linejoin="round"><rect x="3" y="5.5" width="18" height="13" rx="1"/><path d="M3 6.5l9 7 9-7"/></svg>
      liam@tlmbespokehomes.com.au
    </li>
    <li class="contact">
      <svg viewBox="0 0 24 24" fill="none" stroke="var(--green)" stroke-width="1.8" stroke-linejoin="round"><path d="M6.5 3.5l3 3.5-2 2.2a12 12 0 0 0 7.3 7.3l2.2-2 3.5 3-1.8 2.6c-7.5.4-15.3-7.4-14.9-14.9z"/></svg>
      9731205586
    </li>
    <li class="contact">
      <svg viewBox="0 0 24 24" fill="none" stroke="var(--green)" stroke-width="1.8"><circle cx="12" cy="12" r="9"/><ellipse cx="12" cy="12" rx="4" ry="9"/><path d="M3 12h18M4.5 7.5h15M4.5 16.5h15"/></svg>
      tlmbespokehomes.com.au/
    </li>
  </ul>

  <div class="socials">
    <span class="social" aria-label="Professional network profile"></span>
    <span class="social" aria-label="Video channel"></span>
  </div>
</main>
</body>
</html>
```